Business Card for Wellness Clinic

We need a business card for our new logo. I want it to match the feel of the logo

Target Market(s)

Young professional families looking for holistic health care

Industry/Entity Type

Health And Wellness

Contact Information for Business Card

Our business Name: Brackenfield Health & wellness Centre, our phone #, email address...see attached old business card

Font styles to use
Sans Serif

Colors
33b8a4
cee9f5

Requirements
Must have
• my logo and business name
• Font is "Helvetica Neue LT Std 45 Light" and
• Only for "&" using font "Trajan pro bold"
• Use colors in the logo

```html
<!DOCTYPE html>
<html lang="en">
<head>
<meta charset="utf-8">
<title>Brackenfield Health &amp; wellness Centre – Business Card</title>
<link rel="stylesheet" href="https://fonts.googleapis.com/css2?family=Source+Sans+3:wght@300;400;600&display=swap">
<style>
  :root {
    --teal: #33b8a4;
    --sky: #cee9f5;
    --card: #151616;
    --ink-light: #e8eaea;
    --ink-soft: #a9aeae;
    --rule: #bfc4c4;
    --backdrop: #e4e8e9;
  }
  * { margin: 0; padding: 0; box-sizing: border-box; }
  html, body { width: 1200px; height: 814px; overflow: hidden; }
  body {
    background: var(--backdrop);
    font-family: "Source Sans 3", "Helvetica Neue", Arial, sans-serif;
    font-weight: 300;
    position: relative;
  }
  .card {
    position: absolute;
    top: 264px;
    width: 500px;
    height: 286px;
    background: var(--card);
    border-radius: 4px;
    box-shadow: 0 6px 18px rgba(0,0,0,.18);
    color: var(--ink-light);
  }
  .card--front { left: 70px; }
  .card--back { left: 630px; }

  /* Front */
  .brand {
    position: absolute;
    left: 0; right: 0; top: 38px;
    display: flex; flex-direction: column; align-items: center; gap: 14px;
  }
  .brand__square { width: 30px; height: 30px; background: var(--teal); }
  .brand__name {
    font-size: 17px; font-weight: 300; letter-spacing: 2.5px;
    color: var(--ink-light);
  }
  .divider {
    position: absolute; left: 250px; top: 150px;
    width: 1px; height: 96px; background: var(--rule);
  }
  .person {
    position: absolute; right: 265px; top: 196px; text-align: right;
  }
  .person__name { font-size: 20px; font-weight: 600; color: var(--teal); line-height: 1.2; }
  .person__title { font-size: 15px; font-weight: 400; color: var(--ink-soft); }
  .contact {
    position: absolute; left: 264px; top: 148px;
    font-size: 13.5px; font-weight: 400; line-height: 1.45; list-style: none;
  }
  .contact__item { display: flex; align-items: center; gap: 7px; }
  .contact__icon { width: 11px; height: 11px; flex: none; }

  /* Back */
  .back__square {
    position: absolute; right: 30px; top: 22px;
    width: 30px; height: 30px; background: var(--teal);
  }
  .field { position: absolute; display: flex; align-items: flex-end; gap: 6px; }
  .field__label { font-size: 14px; font-weight: 400; color: var(--teal); line-height: 1; }
  .field__line { flex: 1; border-bottom: 1px solid var(--rule); height: 1px; }
  .appointment-title {
    position: absolute; left: 30px; top: 62px;
    font-size: 18px; font-weight: 600; color: var(--teal);
  }
  .field--time { left: 290px; right: 30px; top: 72px; }
  .ampm {
    position: absolute; right: 30px; top: 58px;
    font-size: 9px; color: var(--teal); font-weight: 400;
  }
  .field--date { left: 30px; right: 30px; top: 130px; }
  .field--for { left: 30px; right: 30px; top: 170px; }
  .policy {
    position: absolute; left: 150px; right: 30px; top: 212px;
    font-size: 10.5px; font-weight: 400; line-height: 1.35;
    color: var(--ink-light); text-align: center;
  }
</style>
</head>
<body>

<section class="card card--front" aria-label="Business card front">
  <div class="brand">
    <span class="brand__square"></span>
    <span class="brand__name">Brackenfield Health &amp; wellness Centre</span>
  </div>

  <div class="person">
    <p class="person__name">Dr. Mara Ellison, N.D.</p>
    <p class="person__title">Naturopathic Doctor</p>
  </div>

  <span class="divider"></span>

  <ul class="contact">
    <li class="contact__item">48 Larchmont Ave. W, Suite 210</li>
    <li class="contact__item">Kingsbrook, ON K0X 2B7</li>
    <li class="contact__item">
      <svg class="contact__icon" viewBox="0 0 24 24" aria-hidden="true">
        <path fill="#33b8a4" d="M6.6 10.8a15.1 15.1 0 0 0 6.6 6.6l2.2-2.2a1 1 0 0 1 1-.25 11.4 11.4 0 0 0 3.6.57 1 1 0 0 1 1 1V20a1 1 0 0 1-1 1A17 17 0 0 1 3 4a1 1 0 0 1 1-1h3.5a1 1 0 0 1 1 1c0 1.25.2 2.45.57 3.6a1 1 0 0 1-.25 1z"/>
      </svg>
      555-014-2278
    </li>
    <li class="contact__item">
      <svg class="contact__icon" viewBox="0 0 24 24" aria-hidden="true">
        <path fill="#33b8a4" d="M2 5h20v14H2z"/>
        <path fill="none" stroke="#151616" stroke-width="2" d="M2 6l10 7 10-7"/>
      </svg>
      mellison@larchmontnaturopathic.ca
    </li>
  </ul>
</section>

<section class="card card--back" aria-label="Business card back">
  <span class="back__square"></span>
  <h2 class="appointment-title">Next Appointment</h2>
  <span class="ampm">AM/PM</span>
  <div class="field field--time"><span class="field__label">Time :</span><span class="field__line"></span></div>
  <div class="field field--date"><span class="field__label">Date :</span><span class="field__line"></span></div>
  <div class="field field--for"><span class="field__label">For :</span><span class="field__line"></span></div>
  <p class="policy">If you are unable to keep your appointment, please provide<br>at least 2 business days notice or full visit fees will apply</p>
</section>

</body>
</html>
```